Healthy Supplement featuring Moringa products

Need 3 business card options for our reps to order from Cardloom. Our reps will be ordering from Cardloom once we upload them. Attached is our current designs to show what info needs to be on the cards. Our website is www.tkvitality.com
The business cards will be a template for our reps to order from. Most of our reps are Asian & Hispanic. Please look at our website so you can see who we are to get the look and feel what we need.
Target Market(s)
Adults 30 on up. Health oriented people.
Industry/Entity Type
Health And Wellness
Contact Information for Business Card
Name
Title
Phone
Logo
www.tkvitality.com/my/username
Font styles to use
Requirements
Must have
- Please match our website look and colors. A moringa leaf is nice, but am open to something different.
Nice to have
- Healthy looking and warm, not super cold or too modern.
Should not have
- No harsh colors please.

```html
<!DOCTYPE html>
<html lang="en">
<head>
<meta charset="utf-8">
<title>TK Vitality – Business Card</title>
<link rel="stylesheet" href="https://fonts.googleapis.com/css2?family=Cinzel:wght@400;500&family=Lato:wght@400;700&display=swap">
<style>
  :root {
    --backdrop: #ece9e4;
    --leaf-green: #66a80f;
    --leaf-green-light: #8cc61e;
    --leaf-green-dark: #4f8d0a;
    --paper: #f7f7f9;
    --accent-orange: #f07321;
    --text-light: #ffffff;
  }
  * { margin: 0; padding: 0; box-sizing: border-box; }
  html, body { width: 1200px; height: 900px; overflow: hidden; }
  body {
    position: relative;
    background: var(--backdrop);
    font-family: "Lato", sans-serif;
  }
  .card {
    position: absolute;
    width: 556px;
    height: 343px;
    overflow: hidden;
    box-shadow: 2px 4px 8px rgba(0,0,0,0.25);
  }
  .card-front { left: 330px; top: 90px; background: var(--leaf-green); }
  .card-back {
    left: 330px; top: 470px; width: 559px;
    background: radial-gradient(ellipse at 50% 42%, var(--leaf-green-light) 0%, var(--leaf-green) 60%, var(--leaf-green-dark) 100%);
  }
  .wave { position: absolute; left: 0; top: 0; width: 100%; height: 100%; }
  .leaf-photo {
    position: absolute;
    right: 0; top: 0;
    width: 250px; height: 155px;
    background: radial-gradient(ellipse at 70% 35%, #8fcf4a 0%, rgba(120,190,50,0.6) 45%, rgba(102,168,15,0) 75%);
  }
  .contact { position: absolute; left: 26px; top: 34px; color: var(--text-light); }
  .contact-name {
    font-family: "Cinzel", serif;
    font-weight: 500;
    font-size: 22px;
    letter-spacing: 0.5px;
    line-height: 1.1;
  }
  .contact-title { font-size: 15px; margin-top: 1px; }
  .contact-list { list-style: none; margin-top: 23px; font-size: 15.5px; }
  .contact-list li { display: flex; align-items: center; height: 20.5px; }
  .contact-list svg { width: 11px; height: 11px; margin-right: 7px; fill: var(--text-light); }
  .brand-mark {
    position: absolute;
    display: flex; align-items: center; gap: 10px;
    font-family: "Cinzel", serif;
    font-weight: 500;
    line-height: 1;
    white-space: nowrap;
  }
  .card-front .brand-mark {
    right: 50px; top: 272px;
    color: var(--leaf-green);
    font-size: 32px;
  }
  .card-back .brand-mark {
    left: 0; right: 0; top: 152px;
    justify-content: center;
    color: var(--text-light);
    font-size: 50px;
  }
  .brand-dot { width: 14px; height: 14px; border-radius: 50%; background: currentColor; }
  .card-back .brand-dot { width: 20px; height: 20px; }
</style>
</head>
<body>
  <section class="card card-front">
    <svg class="wave" viewBox="0 0 556 343" preserveAspectRatio="none" aria-hidden="true">
      <path d="M0,196 C50,270 160,272 300,230 C410,196 480,160 556,194 L556,343 L0,343 Z" fill="var(--accent-orange)"/>
      <path d="M0,204 C55,282 170,280 305,240 C415,206 485,172 556,202 L556,343 L0,343 Z" fill="var(--paper)"/>
    </svg>
    <div class="leaf-photo" role="img" aria-label="Close-up photo of moringa leaves"></div>
    <div class="contact">
      <h1 class="contact-name">MARCUS DELGADO</h1>
      <p class="contact-title">Managing Director</p>
      <ul class="contact-list">
        <li><svg viewBox="0 0 12 12"><path d="M1,4 C1,2 3,1.5 6,1.5 C9,1.5 11,2 11,4 L9,4.5 L8.5,3.5 L3.5,3.5 L3,4.5 Z M3,5 L9,5 L10.5,10 L1.5,10 Z"/></svg>044-987 650 321</li>
        <li><svg viewBox="0 0 12 12"><path d="M1,2.5 L11,2.5 L11,3.2 L6,6.5 L1,3.2 Z M1,4.4 L6,7.7 L11,4.4 L11,9.5 L1,9.5 Z"/></svg>info@tkvitality.com</li>
        <li><svg viewBox="0 0 12 12"><circle cx="6" cy="6" r="5"/></svg>www.tkvitality.com/my/username</li>
      </ul>
    </div>
    <div class="brand-mark"><span class="brand-dot"></span>TK Vitality</div>
  </section>

  <section class="card card-back">
    <div class="brand-mark"><span class="brand-dot"></span>TK Vitality</div>
  </section>
</body>
</html>
```